TIDAL VERGE needs bisness cards pronto

Bisness name is "TIDAL VERGE" new bisness the bisness includes lawn mowing, garden matanace, and any jobs around the house.
I need a card that is colorful and vibrant and the bisness of lawn mowing maybe with some nature with it. It also needs my contact details"Darren Quellby mobile 0413562049 call for free quote and email norma.vance@fernmail.com.au and a catchy tag line

Industry/Entity Type

House

Requirements
Must have
• Bisness name "TIDAL VERGE"
Contact details "0413562049"
Email norma.vance@fernmail.com.au
Call for free quote

```html
<!DOCTYPE html>
<html lang="en">
<head>
<meta charset="utf-8">
<title>Tidal Verge – Business Card</title>
<link rel="stylesheet" href="https://fonts.googleapis.com/css2?family=Fira+Sans:wght@400&family=Fira+Mono&display=swap">
<style>
  :root {
    --page-bg: #f2f2f3;
    --card-bg: #403c3c;
    --name-grey: #dcdcde;
    --contact-grey: #b9b9bc;
    --grass-green: #a6cc41;
    --grass-deep: #9cc23a;
    --laser-red: #e8194a;
    --tagline-green: #6f8a45;
  }
  html, body {
    margin: 0;
    padding: 0;
    width: 1200px;
    height: 1000px;
    overflow: hidden;
    background: var(--page-bg);
  }
  .canvas {
    position: relative;
    width: 1200px;
    height: 1000px;
  }
  .business-card {
    position: absolute;
    left: 114px;
    top: 203px;
    width: 972px;
    height: 594px;
    background: var(--card-bg);
    overflow: hidden;
  }
  .business-name {
    position: absolute;
    left: 272px;
    top: 112px;
    margin: 0;
    font-family: "Fira Sans", sans-serif;
    font-weight: 400;
    font-size: 90px;
    line-height: 1;
    letter-spacing: 2px;
    color: var(--name-grey);
    white-space: nowrap;
  }
  .contact-details {
    position: absolute;
    left: 276px;
    top: 212px;
    margin: 0;
    font-family: "Fira Sans", sans-serif;
    font-style: normal;
    font-weight: 400;
    font-size: 21px;
    line-height: 27px;
    color: var(--contact-grey);
    white-space: nowrap;
  }
  .contact-details span {
    display: block;
  }
  .clippings-area {
    position: absolute;
    left: 310px;
    top: 300px;
    width: 662px;
    height: 140px;
    background: radial-gradient(ellipse at 60% 60%, rgba(166, 204, 65, 0.18), rgba(166, 204, 65, 0) 70%);
  }
  .lawn {
    position: absolute;
    left: 0;
    top: 429px;
    width: 972px;
    height: 165px;
    background: linear-gradient(to bottom, var(--grass-deep), var(--grass-green) 45%);
  }
  .laser-beam {
    position: absolute;
    left: 318px;
    top: 443px;
    width: 654px;
    height: 10px;
  }
  .tagline {
    position: absolute;
    left: 14px;
    top: 552px;
    margin: 0;
    font-family: "Fira Mono", monospace;
    font-size: 31px;
    line-height: 1;
    letter-spacing: 8.4px;
    color: var(--tagline-green);
    white-space: nowrap;
  }
</style>
</head>
<body>
  <main class="canvas">
    <section class="business-card">
      <h1 class="business-name">TIDAL VERGE</h1>
      <address class="contact-details">
        <span>Darren Quellby · call for a free quote</span>
        <span>0413562049</span>
        <span>norma.vance@fernmail.com.au</span>
      </address>
      <div class="clippings-area" role="img" aria-label="Grass clippings flying up from the freshly cut lawn"></div>
      <div class="lawn" role="img" aria-label="Row of green grass blades, cut short on the right"></div>
      <svg class="laser-beam" viewBox="0 0 654 10" aria-hidden="true">
        <path d="M5 5 L654 3 L654 8 L5 8 Z" fill="var(--laser-red)"/>
        <circle cx="5" cy="6" r="3.5" fill="var(--laser-red)"/>
      </svg>
      <p class="tagline">gardening in general, to be percise</p>
    </section>
  </main>
</body>
</html>
```